Zumbly - New Payment App for Student

Zum-bly - A Payment App for student to make payment, track own expenses and practice good dietary habits. The App theme is Fun and excitement.
Target User: Secondary Student aged 13-18
Look and Feel: Fun, excitement and simple.
Screen 1
Login to the app using thumbprints or password
Screen 2
Display the balance
Wallet balance >>> go to screen 3 to display transaction history
Gamification balance - points + badges >>> go to screen 3
Button to make payment
Screen 2-1
Allow them to do payment
Click “Pay”
Display QR code
scanning by merchant
Payment made
Notification received
The transaction history will be shown up
Screen 2-2
Allow them to top up (alternatively to parent Top-up using credit card)
Click “Top Up”
Display QR code
Pass the cash to merchant
scanning by merchant
Payment made
Notification received
The new balance will be shown up
Screen 3
Display more details on transaction history
Payment history + gamification history (gain/redeem points)
E.g. 14 Nov Canteen purchase $5.40
- Banana +30 points
- Milk +10 points
Screen 4 (play a game to earn point)
Introduce some trivial games (while waiting in line at cafeteria or school store) to gain some points
Crosswords
Puzzle
Screen 5 (Display achievements)
Leaderboard
Where the individual stands in the class
Where the class stands overall in school
Badges
Level
Achievements
For more, please go to our website http://www.zumbly-pay.example/
Target Market(s)
Secondary School Student aged 13-18
Industry/Entity Type
Education
Logo Text
zumbly
Look and feel

```html
<!DOCTYPE html>
<html lang="en">
<head>
<meta charset="utf-8">
<title>Zumbly – Home</title>
<link href="https://fonts.googleapis.com/css2?family=Lato:wght@300;400;700;900&display=swap" rel="stylesheet">
<style>
  :root{
    --orange:#f47421;
    --orange-light:#ff9a1f;
    --purple-dark:#3b2ba0;
    --purple-mid:#8a3fc0;
    --purple-light:#c883e0;
    --yellow:#ffc928;
    --yellow-dark:#e9a800;
    --green:#6cb52d;
    --text-grey:#555;
    --day-grey:#9a9a9a;
    --band-grey:#ececec;
    --chart-bg:#f8f8f8;
    --white:#fff;
  }
  *{box-sizing:border-box;margin:0;padding:0}
  html,body{width:675px;height:1200px;overflow:hidden;background:var(--white);font-family:"Lato",sans-serif}
  .screen{position:relative;width:675px;height:1200px;overflow:hidden;background:var(--white)}

  .app-header{position:absolute;top:0;left:0;width:100%;height:117px;
    background:linear-gradient(90deg,#f2601a,var(--orange) 50%,var(--orange-light));
    display:flex;align-items:center;justify-content:center}
  .app-header h1{color:var(--white);font-size:30px;font-weight:700}

  .level-banner{position:absolute;top:117px;left:0;width:100%;height:171px;
    background:linear-gradient(90deg,var(--purple-dark),var(--purple-mid) 65%,#b15fd0)}
  .level-banner .banner-tail{position:absolute;top:0;right:0;width:207px;height:100%;
    background:linear-gradient(90deg,var(--purple-light),#b26ad8)}
  .level-banner .pointer{position:absolute;left:460px;bottom:0;width:0;height:0;
    border-left:11px solid transparent;border-right:11px solid transparent;border-bottom:14px solid var(--yellow)}
  .level-badge{position:absolute;left:22px;top:35px;width:100px;height:100px}
  .level-text{position:absolute;left:153px;top:50px;color:var(--white)}
  .level-text .goal{font-size:21px;font-weight:700}
  .level-text .points{font-size:21px;font-weight:400;margin-top:12px}

  .balance{position:absolute;top:288px;left:0;width:100%;height:358px}
  .label{color:var(--text-grey);font-weight:700;font-size:22px;position:absolute}
  .balance .current-label{left:32px;top:18px}
  .balance .current-amount{position:absolute;left:30px;top:38px;font-size:108px;font-weight:300;color:var(--green);letter-spacing:1px}
  .balance .today-label{left:32px;top:233px}
  .balance .week-label{left:374px;top:233px}
  .amount-small{position:absolute;top:278px;font-size:44px;font-weight:300}
  .amount-small.spent{left:30px;color:var(--orange)}
  .amount-small.earned{left:378px;color:var(--green)}

  .divider-band{position:absolute;top:646px;left:0;width:100%;height:11px;background:var(--band-grey)}

  .expense{position:absolute;top:657px;left:0;width:100%;height:457px;background:var(--chart-bg)}
  .expense .expense-label{left:32px;top:26px}
  .weekdays{position:absolute;top:70px;left:0;width:100%;height:30px}
  .weekdays span{position:absolute;transform:translateX(-50%);font-size:20px;color:var(--day-grey)}
  .expense-chart{position:absolute;top:0;left:0}

  .tab-bar{position:absolute;bottom:0;left:0;width:100%;height:86px;background:var(--white);
    border-top:1px solid #eee}
  .tab-icon{position:absolute;top:22px;width:44px;height:44px}
  .pay-button{position:absolute;left:283px;top:1094px;width:108px;height:108px;border-radius:50%;
    background:var(--white);border:9px solid var(--orange);display:flex;align-items:center;justify-content:center}
  .pay-button span{color:var(--orange);font-size:50px;font-weight:900}
</style>
</head>
<body>
<main class="screen">
  <header class="app-header"><h1>Home</h1></header>

  <section class="level-banner">
    <div class="banner-tail"></div>
    <div class="pointer"></div>
    <svg class="level-badge" viewBox="0 0 100 100" aria-label="Level 3 badge">
      <circle cx="50" cy="50" r="49" fill="var(--yellow)"/>
      <circle cx="50" cy="50" r="43" fill="none" stroke="var(--yellow-dark)" stroke-width="2"/>
      <path d="M50 16 L59.5 38 L83 40 L65 56 L70.5 79 L50 67 L29.5 79 L35 56 L17 40 L40.5 38 Z"
            fill="var(--yellow)" stroke="var(--text-grey)" stroke-width="3" stroke-linejoin="round"/>
      <text x="50" y="60" text-anchor="middle" font-family="Lato, sans-serif" font-weight="700" font-size="26" fill="#333">3</text>
    </svg>
    <div class="level-text">
      <p class="goal">500 point to go to reach level 4!</p>
      <p class="points">Your have 2500 points</p>
    </div>
  </section>

  <section class="balance">
    <p class="label current-label">Current balance</p>
    <p class="current-amount">$ 35.00</p>
    <p class="label today-label">Today</p>
    <p class="amount-small spent">($ 4.50)</p>
    <p class="label week-label">This week</p>
    <p class="amount-small earned">$ 20.00</p>
  </section>

  <div class="divider-band"></div>

  <section class="expense">
    <svg class="expense-chart" width="675" height="457" viewBox="0 0 675 457" aria-label="Weekly expense line chart">
      <defs>
        <linearGradient id="expenseStroke" x1="0" y1="150" x2="0" y2="410" gradientUnits="userSpaceOnUse">
          <stop offset="0" stop-color="#ffd040"/>
          <stop offset="1" stop-color="#f47a25"/>
        </linearGradient>
      </defs>
      <path d="M0 326 Q70 265 97 259 Q120 256 150 305 Q170 345 194 367 Q240 392 288 401
               Q300 400 318 330 Q355 158 387 158 Q410 160 450 220 Q470 240 484 243
               Q520 270 560 272 L675 272"
            fill="none" stroke="url(#expenseStroke)" stroke-width="9" stroke-linecap="round" stroke-linejoin="round"/>
    </svg>
    <p class="label expense-label">Expense</p>
    <div class="weekdays">
      <span style="left:97px">Mon</span>
      <span style="left:194px">Tue</span>
      <span style="left:288px">Wed</span>
      <span style="left:387px">Thu</span>
      <span style="left:484px">Fri</span>
      <span style="left:581px">Sat</span>
    </div>
  </section>

  <nav class="tab-bar">
    <svg class="tab-icon" style="left:59px" viewBox="0 0 44 44" aria-label="Home">
      <path d="M5 21 L22 6 L39 21 M10 17 V38 H18 V27 H26 V38 H34 V17" fill="none" stroke="var(--orange)" stroke-width="3" stroke-linejoin="round" stroke-linecap="round"/>
    </svg>
    <svg class="tab-icon" style="left:176px" viewBox="0 0 44 44" aria-label="Transactions">
      <path d="M6 15 H36 M14 7 L6 15 L14 23 M38 29 H8 M30 21 L38 29 L30 37" fill="none" stroke="#333" stroke-width="3" stroke-linecap="round" stroke-linejoin="round"/>
    </svg>
    <svg class="tab-icon" style="left:455px" viewBox="0 0 44 44" aria-label="Games">
      <path d="M12 12 H32 Q41 12 42 26 Q42 34 36 33 Q32 32 29 27 H15 Q12 32 8 33 Q2 34 2 26 Q3 12 12 12 Z" fill="none" stroke="#333" stroke-width="2.6" stroke-linejoin="round"/>
      <path d="M12 17 V25 M8 21 H16" stroke="#333" stroke-width="2.6" stroke-linecap="round"/>
      <circle cx="30" cy="18" r="1.8" fill="#333"/><circle cx="34" cy="22" r="1.8" fill="#333"/>
    </svg>
    <svg class="tab-icon" style="left:573px" viewBox="0 0 44 44" aria-label="Profile">
      <circle cx="22" cy="14" r="9" fill="none" stroke="#333" stroke-width="2.6"/>
      <path d="M6 41 Q6 27 22 26 Q38 27 38 41 Z" fill="none" stroke="#333" stroke-width="2.6" stroke-linejoin="round"/>
      <path d="M18 27 L22 34 L26 27" fill="none" stroke="#333" stroke-width="2.2"/>
    </svg>
  </nav>
  <div class="pay-button" aria-label="Pay"><span>$</span></div>
</main>
</body>
</html>
```